Brightwell Wiring Needs A Logo Design

We need a logo for my new company based out of Sacramento, Ca called Brightwell Wiring. The name says it all, my electrical contracting business provides "Brightwell Craftsman Work" I'm open to any colors that pop and customers to say Wow. I would love to print my cards on metal.

Contact Information for Business Card

The card needs to have as follows
Name of company: Brightwell Wiring
My Name: Marco Delvane
Phone # 916-555-0147
CL# 4873920
Email: brightwellwiring@mailtorva.com
and a slogan that represent "BRIGHTWELL"

Requirements
Must have
• The card needs to have as follows
• Name of company: Brightwell Wiring
• My Name : Marco Delvane
• Phone # 916-555-0147
• CL# 4873920
• Email: brightwellwiring@mailtorva.com
• and a slogan that represent "BRIGHTWELL"
Nice to have
• popping colors
• electrical Arcing

```html
<!DOCTYPE html>
<html lang="en">
<head>
<meta charset="utf-8">
<title>Brightwell Wiring – Business Card</title>
<link href="https://fonts.googleapis.com/css2?family=Montserrat:wght@500;600&family=Lato:wght@400;700&display=swap" rel="stylesheet">
<style>
  :root {
    --backdrop: #d6d6d6;
    --card: #f4f4f2;
    --brand-blue: #1c4f8f;
    --ink: #141414;
    --ink-soft: #3a3a3a;
    --hatch: #a9a9a9;
  }
  * { box-sizing: border-box; margin: 0; padding: 0; }
  html, body {
    width: 1200px; height: 900px; overflow: hidden;
    background: var(--backdrop);
    font-family: "Lato", Arial, sans-serif;
  }
  .sheet {
    width: 1200px; height: 900px;
    display: flex; flex-direction: column;
    align-items: center; justify-content: center; gap: 40px;
  }
  .card {
    position: relative;
    width: 580px; height: 332px;
    background: var(--card);
    box-shadow: 0 6px 18px rgba(0,0,0,0.18);
    overflow: hidden;
  }

  /* Wordmark */
  .wordmark {
    display: flex; align-items: center; gap: 14px;
    font-family: "Montserrat", Arial, sans-serif;
    font-weight: 600;
    color: var(--ink);
    line-height: 1;
    white-space: nowrap;
  }
  .wordmark__dot {
    width: 16px; height: 16px; border-radius: 50%;
    background: var(--brand-blue); flex: none;
  }

  /* Front */
  .card--front .brand {
    position: absolute; left: 0; right: 0; top: 84px;
    display: flex; flex-direction: column; align-items: center; gap: 16px;
  }
  .card--front .wordmark {
    font-size: 40px; letter-spacing: 0.5px;
  }
  .slogan {
    font-family: "Lato", Arial, sans-serif;
    font-size: 15px; font-weight: 400;
    letter-spacing: 4px; text-transform: uppercase;
    color: var(--ink-soft);
  }
  .card--front .band {
    position: absolute; left: 0; right: 0;
    top: 232px; height: 56px;
    background: var(--brand-blue);
  }

  /* Back */
  .card--back .wordmark {
    position: absolute; left: 22px; top: 156px;
    font-size: 19px; gap: 9px;
  }
  .card--back .wordmark__dot { width: 10px; height: 10px; }
  .divider-stripe {
    position: absolute; top: 0; bottom: 0; left: 262px; width: 16px;
    background: var(--brand-blue);
  }
  .divider-stripe__texture {
    position: absolute; left: 258px; width: 24px; top: 78px; height: 170px;
    background: linear-gradient(180deg, #bdbdbd, var(--hatch));
  }
  .contact {
    position: absolute; left: 312px; top: 70px; right: 26px;
  }
  .contact__name {
    font-size: 24px; font-weight: 400; letter-spacing: 1px;
    color: var(--ink); text-transform: uppercase;
    padding-bottom: 4px;
    border-bottom: 2px solid var(--brand-blue);
  }
  .contact__licence {
    margin-top: 4px;
    font-size: 14px; letter-spacing: 1px; color: var(--ink-soft);
  }
  .contact__list { list-style: none; margin-top: 26px; }
  .contact__item {
    display: flex; align-items: center; gap: 10px;
    font-size: 13px; color: var(--ink-soft);
    margin-bottom: 12px;
  }
  .contact__icon {
    width: 18px; height: 18px; border-radius: 3px;
    background: var(--brand-blue);
    display: flex; align-items: center; justify-content: center; flex: none;
  }
</style>
</head>
<body>
<main class="sheet">

  <section class="card card--front" aria-label="Card front">
    <div class="brand">
      <div class="wordmark"><span class="wordmark__dot"></span>Brightwell Wiring</div>
      <p class="slogan">Brightwell Craftsman Work</p>
    </div>
    <div class="band"></div>
  </section>

  <section class="card card--back" aria-label="Card back">
    <div class="wordmark"><span class="wordmark__dot"></span>Brightwell Wiring</div>

    <div class="divider-stripe"></div>
    <div class="divider-stripe__texture" role="img" aria-label="Diagonal grey hatched texture on the blue divider"></div>

    <div class="contact">
      <h1 class="contact__name">Marco Delvane</h1>
      <p class="contact__licence">CL# 4873920</p>
      <ul class="contact__list">
        <li class="contact__item">
          <span class="contact__icon">
            <svg width="12" height="12" viewBox="0 0 24 24" aria-hidden="true">
              <path fill="#fff" d="M6.6 10.8a15 15 0 0 0 6.6 6.6l2.2-2.2a1 1 0 0 1 1-.25 11.4 11.4 0 0 0 3.6.57 1 1 0 0 1 1 1V20a1 1 0 0 1-1 1A17 17 0 0 1 3 4a1 1 0 0 1 1-1h3.5a1 1 0 0 1 1 1c0 1.25.2 2.45.57 3.57a1 1 0 0 1-.25 1z"/>
            </svg>
          </span>
          916-555-0147
        </li>
        <li class="contact__item">
          <span class="contact__icon">
            <svg width="12" height="12" viewBox="0 0 24 24" aria-hidden="true">
              <rect x="2" y="5" width="20" height="14" rx="1.5" fill="#fff"/>
              <path d="M3 6.5l9 6.5 9-6.5" fill="none" stroke="#1c4f8f" stroke-width="2"/>
            </svg>
          </span>
          brightwellwiring@mailtorva.com
        </li>
      </ul>
    </div>
  </section>

</main>
</body>
</html>
```